Erstellung von Datenblatt-Template
Zielgruppe
Informationen über ins finden Sie hier:
https://www.tovrel-de.de/unternehmen
Aufgabenstellung
Bitte erstellen Sie anhand von den folgenden Produkten:
Produkt A: https://www.tovrel-de.de/produkte/flexible-led-leisten/flexible-led-leiste-kalt-weiss-mit-flat-top-leds
Produkt B: https://www.tovrel-de.de/produkte/lagerartikel/led-einheit-rq71-5w
Datenblatt-Templates. Produkt A hat 3 Bilder und viel Text und Produkt B hat 1 Bild und wenig Text. Bei Produkt A fügen Sie bitte noch einen Platzhalter für eine Kurzbeschreibung hinzu, um “viel Text” zu simulieren.
Wichtig ist, dass es für uns zukünftig einfach ist dieses Template zu bearbeiten um Datenblätter für all unsere Produkte selber erstellen zu können. Hier sollten uns dann mehrere Templates zur Auswahl stehen (Typ A: viel Text, Typ B: wenig Text. Des Weiteren soll es die Möglichkeit geben die Anzahl der Bilder einfach zu bestimmen (mindestens 1, höchstens 3).
Bitte beschreiben Sie auch kurz wie die Bearbeitung auf unserer Seite aussehen würde, wenn wir uns für dieses Template entscheiden würden. Dies soll so einfach wie möglich gestaltet sein, da wir nur einfache Bearbeitungen wie Text/Bilder einfügen oder ähnliches vornehmen können.
Das Template soll professionell und übersichtlich sein. Die Farbkombinationen sind Ihnen überlassen, jedoch bitte nicht allzu bunt. Im Datenblatt sollen folgende Informationen angegeben sein:
• Überschrift: Produktdatenblatt
• Name des Produktes
• Produktbild/Bilder
• Kurzbeschreibung des Produktes
• Technische Daten (Als Tabelle)
• Eine Auswahl aus den Icons „Icons.zip“ im Anhang (welche Icons bei welchem Produkt angezeigt werden sollte dann auch von uns definierbar sein):
• Footer mit Firmenlogo (im Anhang) und Kontaktdaten (Daten: https://www.tovrel-de.de/impressum)

```html
<!DOCTYPE html>
<html lang="de">
<head>
<meta charset="utf-8">
<title>Produktdatenblatt – Flexible LED Leiste Kalt Weiß</title>
<link rel="stylesheet" href="https://fonts.googleapis.com/css2?family=Roboto+Condensed:wght@400&family=Arimo:wght@400;700&display=swap">
<style>
  :root{
    --accent:#8e1c4a;
    --ink:#1a1a1a;
    --panel:#ebebeb;
    --footer:#e3e3e3;
    --rule:#222;
  }
  html,body{margin:0;padding:0;overflow:hidden;}
  body{width:849px;height:1200px;position:relative;background:#fff;color:var(--ink);font-family:"Arimo",Arial,sans-serif;}
  .sheet-title{position:absolute;left:81px;top:76px;margin:0;font:400 33px/1 "Roboto Condensed",sans-serif;letter-spacing:.2px;}
  .product-band{position:absolute;left:0;top:127px;width:540px;height:31px;background:var(--panel);border-bottom:3px solid var(--accent);}
  .product-band h2{margin:0;position:absolute;left:81px;top:6px;font:400 20px/1 "Roboto Condensed",sans-serif;}
  .brand{position:absolute;left:672px;top:104px;font:400 22px/1 "Roboto Condensed",sans-serif;color:var(--accent);letter-spacing:1px;}
  .intro{position:absolute;left:81px;top:190px;width:688px;font-size:12.9px;line-height:16.2px;text-align:justify;hyphens:auto;-webkit-hyphens:auto;}
  .intro p{margin:0 0 16px;}
  .spec-panel{position:absolute;left:225px;top:382px;width:315px;height:553px;background:var(--panel);border-top:4px solid var(--accent);}
  .spec-row{position:absolute;left:81px;width:459px;}
  .spec-row .label{position:absolute;left:6px;top:14px;font-size:12.6px;}
  .spec-row .value{position:absolute;left:159px;top:13px;width:268px;font-size:12.2px;line-height:15.3px;}
  .label-rule{position:absolute;left:0;bottom:-1px;width:135px;border-bottom:1px solid var(--rule);}
  .value-rule{position:absolute;left:144px;width:315px;bottom:-1px;border-bottom:1px solid var(--rule);}
  .row-name{top:386px;height:44px;}
  .row-info{top:430px;height:415px;}
  .row-check{top:845px;height:89px;}
  .features{list-style:none;margin:0;padding:0;}
  .features li{position:relative;padding-left:13px;margin-bottom:10px;font-size:12.2px;line-height:15.3px;}
  .features li::before{content:"";position:absolute;left:0;top:3px;width:7px;height:7px;background:var(--accent);}
  .badge{position:absolute;left:163px;top:15px;}
  .photo{position:absolute;left:578px;width:267px;border:2px solid var(--accent);}
  .photo-1{top:382px;height:175px;background:radial-gradient(ellipse at 40% 55%,#e8ecef 0%,#8d9398 30%,#3a3a3a 70%,#262626 100%);}
  .photo-2{top:567px;height:176px;background:radial-gradient(ellipse at 40% 55%,#f3efe4 0%,#a9a396 30%,#3c3a36 70%,#272624 100%);}
  .photo-3{top:754px;height:175px;background:radial-gradient(ellipse at 40% 55%,#f6dcb4 0%,#b39670 30%,#3e3527 70%,#272320 100%);}
  .footer{position:absolute;left:0;top:1108px;width:849px;height:92px;background:var(--footer);border-top:4px solid var(--accent);text-align:center;font-size:12.4px;line-height:15.6px;}
  .footer .company{font-weight:700;margin-top:13px;margin-bottom:5px;}
  .footer p{margin:0;}
</style>
</head>
<body>
  <h1 class="sheet-title">PRODUKTDATENBLATT</h1>
  <div class="brand">TOVREL</div>

  <div class="product-band"><h2>FLEXIBLE LED LEISTE KALT WEISS MIT FLAT TOP LEDS</h2></div>

  <section class="intro">
    <p>Soluptae eum ipis volentotam, quid ut aliquas sa nobis dolut aspedit que se seritam, et autatur? Bisqui abor as aut quatatu rerovid quias ped magnimus es sitium laciatur, verum adio. Odi dolupta sumquo consequam inus quae nis ipis reptas es same dolorepudae vellant ad quae ventium hictam inumquos re cum enderum quam volesto officite con nonseque comni bea vit eiunti doluptatus Ati isci occus expliam eum es rempore conseque alibero qui aditium nis dios raercillant estent poratiisci dit et qui consequi dolorio nsecepro bearci quam.</p>
    <p>tam, quid ut aliquas sa nobis dolut aspedit que se seritam, et autatur? Bisqui abor as aut quatatu rerovid quias ped mag&shy;nimus es sitium laciatur, verum adio. Odi dolupta sumquo consequam inus quae nis ipis reptas es same dolorepudae vel&shy;lant ad quae ventium hictam inumquos re cum enderum quam volesto officite con nonseque comni bea vit eiunti dolupta&shy;tus Ati isci occus expli</p>
  </section>

  <div class="spec-panel"></div>

  <div class="spec-row row-name">
    <div class="label">Produktbezeichnung</div>
    <div class="value">Flexible LED Leiste Kalt Weiß<br>mit Flat Top LEDs</div>
    <div class="label-rule"></div><div class="value-rule"></div>
  </div>

  <div class="spec-row row-info">
    <div class="label">Produktinformation</div>
    <div class="value">
      <ul class="features">
        <li>Sehr gut geeignet für die Beleuchtung und Hinterleuchtung von PoS Displays.</li>
        <li>Farbtemperatur ca. 6000 Kelvin.</li>
        <li>Effizient und hell mit nur geringer Wärmeentwicklung.</li>
        <li>Flexible LED Leiste, Breite 10mm,<br>alle 10cm mit einer Schere teilbar.</li>
        <li>Die Rückseite ist mit einem Vexa Klebestreifen für eine schnelle Montage ausgerüstet.</li>
        <li>6 Leuchtdioden wasserklar transparent weiß leuchtend (ultrahell) pro 10cm.</li>
        <li>Leuchtdioden mit 120° Abstrahlwinkel.</li>
        <li>Farbwiedergabeindex: min. 80Ra für eine natürliche Farbwiedergabe.</li>
        <li>Betriebsspannung: 24Volt DC</li>
        <li>Dimmbar (Dimmer, siehe Zubehör).</li>
        <li>Bis zu 2 m können mit unserem Stecker-<br>netzteil 24V/1A (siehe Zubehör) versorgt werden.</li>
      </ul>
    </div>
    <div class="label-rule"></div><div class="value-rule"></div>
  </div>

  <div class="spec-row row-check">
    <div class="label">Prüfzeichen</div>
    <svg class="badge" width="50" height="50" viewBox="0 0 50 50" role="img" aria-label="Prüfzeichen">
      <rect x="2" y="2" width="46" height="46" rx="6" fill="#fff" stroke="#222" stroke-width="2"/>
    </svg>
    <div class="label-rule"></div><div class="value-rule"></div>
  </div>

  <div class="photo photo-1" role="img" aria-label="Aufgerollte LED Leiste, kaltweiß leuchtend"></div>
  <div class="photo photo-2" role="img" aria-label="Aufgerollte LED Leiste, neutralweiß leuchtend"></div>
  <div class="photo photo-3" role="img" aria-label="Aufgerollte LED Leiste, warmweiß leuchtend"></div>

  <footer class="footer">
    <p class="company">Tovrel Lichtsysteme GmbH</p>
    <p>Hafenring 14 | 47051 Duisburg | Germany</p>
    <p>Telefon: 0203 - 48 62 30 | Fax: 0203 - 48 62 311 | E-Mail: info@tovrel-de.de | www.tovrel-de.de</p>
    <p>Geschäftsführer: Jens Marlow | Amtsgericht Duisburg, HRB 4817 | Umsatzsteuer-ID: DE305718264 | WEEE-Reg.-Nr.: DE 61940275</p>
  </footer>
</body>
</html>
```